HVAC Door Hanger- 4.25 inches by 11 inches

Hello We are using the Brightvale door hanger as an inspiration for our new door hanger. The company name is Corvant Home Services. Logo files attached. The Slogan needs to be added on the front with the Logo "Southern California’s Trusted Name in Home Services". Instead of the X protection plan, the name will be Full Shield by Corvant or Corvant Climate Keeper- The slogan for this package will be "Peace of Mind, For Every Season

```html
<!DOCTYPE html>
<html lang="en">
<head>
<meta charset="utf-8">
<title>Corvant Home Services – Door Hanger</title>
<link href="https://fonts.googleapis.com/css2?family=Oswald:wght@300;400;500;700&family=Montserrat:wght@500;600;800&display=swap" rel="stylesheet">
<style>
:root{
  --page:#6a7b7d;
  --white:#ffffff;
  --red:#f5120f;
  --blue:#2688d6;
  --orange:#f7900f;
  --ink:#111111;
  --yellow:#f4f013;
  --photo-a:#c9ccd0;
  --photo-b:#3c4b66;
}
*{margin:0;padding:0;box-sizing:border-box}
html,body{width:1200px;height:1200px;overflow:hidden;background:var(--page)}
.canvas{position:relative;width:1200px;height:1200px}
.hanger{position:absolute;left:106px;width:988px;height:381px;background:var(--white);overflow:hidden;box-shadow:4px 6px 12px rgba(0,0,0,.35)}
.hanger--front{top:199px}
.hanger--back{top:620px}
.hole{position:absolute;left:800px;top:132px;width:116px;height:116px;border-radius:50%;background:var(--page);z-index:5}
.side-drop{position:absolute;left:931px;top:174px;width:120px;height:137px;border-radius:60px 0 60px 60px;background:var(--orange);transform:rotate(-45deg);transform-origin:center}
/* front */
.slogan-band{position:absolute;left:0;top:17px;width:714px;height:123px;background:var(--red)}
.slogan-band__lead{position:absolute;left:30px;top:14px;font:700 54px/1 'Oswald',sans-serif;color:var(--white);letter-spacing:.5px}
.slogan-band__rest{position:absolute;left:30px;top:70px;font:400 38px/1 'Oswald',sans-serif;color:var(--white)}
.technician-photo{position:absolute;left:698px;top:0;width:290px;height:140px;background:linear-gradient(120deg,var(--photo-b) 0%,#6d7788 45%,var(--photo-a) 100%)}
.brand-rule{position:absolute;left:34px;top:159px;width:6px;height:139px;background:var(--blue)}
.brand-name{position:absolute;left:74px;top:176px;font:600 44px/1 'Montserrat',sans-serif;color:var(--blue);letter-spacing:1px;white-space:nowrap}
.services{position:absolute;left:74px;top:265px;font:600 22px/1 'Montserrat',sans-serif;color:var(--red);letter-spacing:4.6px;white-space:nowrap}
/* contact band */
.contact-band{position:absolute;left:0;top:318px;width:988px;height:63px}
.contact-band svg{position:absolute;inset:0}
.contact__phone{position:absolute;left:280px;top:6px;font:700 40px/1.2 'Oswald',sans-serif;color:var(--ink)}
.contact__web{position:absolute;left:595px;top:12px;font:500 29px/1.2 'Oswald',sans-serif;color:var(--white)}
/* back */
.season-band{position:absolute;left:0;top:17px;width:448px;height:54px;background:var(--blue);padding-left:23px;font:500 33px/54px 'Oswald',sans-serif;color:var(--white)}
.season-list{position:absolute;left:23px;top:86px;width:410px;list-style:none;font:400 15.5px/1.12 'Oswald',sans-serif;color:var(--ink)}
.season-list li{position:relative;padding-left:24px;margin-bottom:12px}
.season-list svg{position:absolute;left:0;top:4px;width:11px;height:11px}
.plan-band{position:absolute;left:456px;top:17px;width:532px;height:123px;background:var(--red)}
.plan-band__title{position:absolute;left:0;width:522px;top:7px;text-align:center;font:800 29px/1 'Montserrat',sans-serif;color:var(--white)}
.plan-band__price{position:absolute;left:0;width:522px;top:39px;text-align:center;font:500 17px/1 'Montserrat',sans-serif;color:var(--white)}
.plan-band__price b{font-weight:800}
.limited{position:absolute;left:870px;top:78px;width:118px;height:62px;background:var(--blue);text-align:center;font:700 19px/1 'Oswald',sans-serif;color:var(--yellow);padding-top:6px;-webkit-text-stroke:.6px #000;white-space:nowrap}
.limited span{display:block;font-size:27px}
.coupon{position:absolute;left:469px;top:79px;width:390px;height:220px;background:var(--orange);border-radius:12px}
.coupon__stub{position:absolute;left:20px;top:22px;width:119px;height:173px;background:var(--red)}
.coupon__stub-frame{position:absolute;left:20px;top:20px;width:89px;height:138px;border:1px dashed var(--white);display:flex;align-items:center;justify-content:center}
.coupon__stub-text{transform:rotate(-90deg);font:700 27px/.95 'Oswald',sans-serif;color:var(--white);text-align:center;white-space:nowrap}
.coupon__body{position:absolute;left:139px;top:22px;width:218px;height:173px;background:var(--white)}
.coupon__kicker{position:absolute;left:21px;top:12px;font:800 14px/1 'Montserrat',sans-serif;color:var(--blue)}
.coupon__deal{position:absolute;left:20px;top:32px;font:700 44px/1 'Oswald',sans-serif;color:var(--red);white-space:nowrap}
.coupon__terms{position:absolute;left:24px;top:90px;width:167px;height:68px;border:1px dashed var(--blue);list-style:none;padding:6px 0 0 10px;font:400 9.5px/13.5px 'Oswald',sans-serif;color:var(--ink)}
.coupon__terms li::before{content:"";display:inline-block;width:6px;height:6px;border-radius:50%;background:var(--red);margin-right:5px}
.perf{position:absolute;left:20px;width:337px;height:6px;background:radial-gradient(circle at 3px 3px,var(--orange) 2.4px,transparent 2.6px) 0 0/12px 6px repeat-x}
</style>
</head>
<body>
<main class="canvas">

  <section class="hanger hanger--front" aria-label="Door hanger front">
    <div class="slogan-band">
      <p class="slogan-band__lead">SOUTHERN CALIFORNIA’S</p>
      <p class="slogan-band__rest">Trusted Name in Home Services</p>
    </div>
    <div class="technician-photo" role="img" aria-label="Photo of a technician in a blue hard hat adjusting pipes with a wrench"></div>
    <div class="hole"></div>
    <div class="side-drop"></div>
    <div class="brand-rule"></div>
    <p class="brand-name">CORVANT HOME SERVICES</p>
    <p class="services">HEATING COOLING PLUMBING ELECTRICAL</p>
    <div class="contact-band">
      <svg width="988" height="63" viewBox="0 0 988 63">
        <polygon points="170,0 526,0 594,63 238,63" fill="#f7900f"/>
        <polygon points="526,0 988,0 988,63 594,63" fill="#2688d6"/>
        <circle cx="251" cy="32" r="17" fill="#f5120f"/>
        <rect x="245" y="22" width="12" height="20" rx="2" fill="none" stroke="#fff" stroke-width="2"/>
        <circle cx="566" cy="32" r="17" fill="#f5120f"/>
        <circle cx="566" cy="32" r="9" fill="none" stroke="#fff" stroke-width="1.8"/>
        <path d="M557 32h18M566 23c-4 5-4 13 0 18M566 23c4 5 4 13 0 18" fill="none" stroke="#fff" stroke-width="1.5"/>
      </svg>
      <p class="contact__phone">0655 (321) 870</p>
      <p class="contact__web">www.corvanthomeservices.com</p>
    </div>
  </section>

  <section class="hanger hanger--back" aria-label="Door hanger back">
    <h2 class="season-band">Peace of Mind, For Every Season</h2>
    <ul class="season-list">
      <li><svg viewBox="0 0 12 12"><circle cx="6" cy="6" r="5" fill="none" stroke="#f5120f" stroke-width="1.2"/><path d="M3.5 6l2 2 4-5" fill="none" stroke="#333" stroke-width="1.4"/></svg>Sed ut perspiciatis unde omnis iste natus error sit voluptatem accusantium doloremque laudantium,</li>
      <li><svg viewBox="0 0 12 12"><circle cx="6" cy="6" r="5" fill="none" stroke="#f5120f" stroke-width="1.2"/><path d="M3.5 6l2 2 4-5" fill="none" stroke="#333" stroke-width="1.4"/></svg>But I must explain to you how all this mistaken idea of denouncing pleasure and praising pain was born and I will give you a complete account of the system, and expound the actual teachings of the great explorer of the truth,</li>
      <li><svg viewBox="0 0 12 12"><circle cx="6" cy="6" r="5" fill="none" stroke="#f5120f" stroke-width="1.2"/><path d="M3.5 6l2 2 4-5" fill="none" stroke="#333" stroke-width="1.4"/></svg>On the other hand, we denounce with righteous indignation and dislike men who are</li>
      <li><svg viewBox="0 0 12 12"><circle cx="6" cy="6" r="5" fill="none" stroke="#f5120f" stroke-width="1.2"/><path d="M3.5 6l2 2 4-5" fill="none" stroke="#333" stroke-width="1.4"/></svg>Praising pain was born and I will give you a complete account of the system, and expound the actual teachings</li>
    </ul>
    <div class="plan-band">
      <h3 class="plan-band__title">FULL SHIELD BY CORVANT</h3>
      <p class="plan-band__price"><b>$XXX</b>/MONTH TO <b>$XXX</b>/MONTH</p>
    </div>
    <div class="coupon">
      <div class="coupon__stub">
        <div class="coupon__stub-frame"><p class="coupon__stub-text">DISCOUNT<br>COUPON</p></div>
      </div>
      <div class="coupon__body">
        <p class="coupon__kicker">VOUCHER SHOPPING</p>
        <p class="coupon__deal">75% OFF</p>
        <ul class="coupon__terms">
          <li>Covers yearly system tune-ups</li>
          <li>No overtime charges</li>
          <li>Priority visits across the region</li>
          <li>Ask for full plan terms</li>
        </ul>
      </div>
      <div class="perf" style="top:19px"></div>
      <div class="perf" style="top:192px"></div>
    </div>
    <div class="limited">LIMITED TIME<span>OFFER!</span></div>
    <div class="hole" style="top:133px"></div>
    <div class="side-drop"></div>
    <div class="contact-band">
      <svg width="988" height="63" viewBox="0 0 988 63">
        <polygon points="170,0 526,0 594,63 238,63" fill="#f7900f"/>
        <polygon points="526,0 988,0 988,63 594,63" fill="#2688d6"/>
        <circle cx="251" cy="32" r="17" fill="#f5120f"/>
        <rect x="245" y="22" width="12" height="20" rx="2" fill="none" stroke="#fff" stroke-width="2"/>
        <circle cx="566" cy="32" r="17" fill="#f5120f"/>
        <circle cx="566" cy="32" r="9" fill="none" stroke="#fff" stroke-width="1.8"/>
        <path d="M557 32h18M566 23c-4 5-4 13 0 18M566 23c4 5 4 13 0 18" fill="none" stroke="#fff" stroke-width="1.5"/>
      </svg>
      <p class="contact__phone">0655 (321) 870</p>
      <p class="contact__web">www.corvanthomeservices.com</p>
    </div>
  </section>

</main>
</body>
</html>
```